Business Card Design Project for Electrical Company

We need a business card designed for a new Electrical Company called Dorvel Electrical Solutions, i dont mind if only Dorvel Electrical is used. We are a domestic and commercial Electrical Company that provides a range of Electrical Services. Our Company colours are Fluro Yellow and Black with the Lightning bolt picture attached.I have attached a card that has been made i think it is rather basic and am looking for something more. the font of Dorvel Electrical has been used on our car graphics as well as the lightning bolt. i want to keep them the same so we can brand our business. Some things we want on the front of the card are Dorvel Electrical Solutions, Owen Platt, 0438516274, admin@dorvelelectrical.example, Lic No 58342, Servicing CQ Region. But we want Owens name seperate to the phone number as its the phone number for the office, owen wont be answering the phone so we are thinking we dont want to give that impression. What do you think? with all that if you have complete different font designs please submit what you think would work best. keeping in mind our company name and details as well as coulors.

Industry/Entity Type

Business

```html
<!DOCTYPE html>
<html lang="en">
<head>
<meta charset="utf-8">
<title>Dorvel Electrical Solutions – Business Card</title>
<link rel="stylesheet" href="https://fonts.googleapis.com/css2?family=Crimson+Text:wght@400;600&family=Oswald:wght@400;500&display=swap">
<style>
  :root {
    --fluro: #e9f000;
    --ink: #111111;
    --paper: #ffffff;
    --spark: #d9dbe2;
  }
  html, body {
    margin: 0;
    padding: 0;
    overflow: hidden;
    background: var(--paper);
  }
  .card {
    position: relative;
    width: 1200px;
    height: 700px;
    overflow: hidden;
    background: var(--paper);
    font-family: "Crimson Text", serif;
  }
  .card__bolt {
    position: absolute;
    left: 0;
    top: 0;
    width: 340px;
    height: 290px;
    background: radial-gradient(ellipse at 70% 10%, var(--spark) 0%, rgba(217, 219, 226, 0.45) 40%, rgba(255, 255, 255, 0) 75%);
  }
  .card__wave {
    position: absolute;
    inset: 0;
    width: 1200px;
    height: 700px;
  }
  .brand {
    position: absolute;
    left: 70px;
    top: 30px;
    margin: 0;
    color: var(--ink);
    font-family: "Crimson Text", serif;
    font-weight: 600;
    text-transform: uppercase;
    line-height: 1;
  }
  .brand__line {
    display: block;
  }
  .brand__line--first,
  .brand__line--second {
    font-size: 88px;
    letter-spacing: 2px;
  }
  .brand__line--second {
    margin-top: -6px;
  }
  .brand__line--third {
    font-size: 46px;
    letter-spacing: 6px;
    margin-top: 4px;
    padding-left: 176px;
  }
  .person {
    position: absolute;
    right: 40px;
    top: 48px;
    text-align: right;
  }
  .person__name {
    margin: 0;
    font-family: "Oswald", sans-serif;
    font-weight: 400;
    font-size: 56px;
    line-height: 1;
    color: var(--ink);
  }
  .person__role {
    margin: 6px 0 0;
    font-size: 21px;
    color: var(--ink);
  }
  .region {
    position: absolute;
    right: 28px;
    top: 350px;
    margin: 0;
    font-family: "Oswald", sans-serif;
    font-weight: 500;
    font-size: 40px;
    line-height: 1;
    text-transform: uppercase;
    letter-spacing: 1px;
    color: var(--ink);
  }
  .contact__phone {
    position: absolute;
    right: 28px;
    top: 580px;
    margin: 0;
    font-size: 38px;
    font-weight: 600;
    color: var(--ink);
  }
  .contact__email {
    position: absolute;
    right: 20px;
    top: 636px;
    margin: 0;
    font-size: 40px;
    color: var(--paper);
  }
  .licence {
    position: absolute;
    left: 28px;
    top: 644px;
    margin: 0;
    font-size: 40px;
    color: var(--paper);
  }
</style>
</head>
<body>
  <div class="card">
    <div class="card__bolt" role="img" aria-label="Lightning bolt artwork used on the company vehicles"></div>

    <svg class="card__wave" viewBox="0 0 1200 700" aria-hidden="true">
      <path fill="var(--fluro)" d="M0 410 C60 345 250 318 420 330 C560 342 640 385 760 362 C900 332 1010 190 1200 188 L1200 700 L0 700 Z"/>
      <path fill="none" stroke="var(--ink)" stroke-width="3" d="M0 410 C60 345 250 318 420 330 C560 342 640 385 760 362 C900 332 1010 190 1200 188"/>
    </svg>

    <h1 class="brand">
      <span class="brand__line brand__line--first">Dorvel</span>
      <span class="brand__line brand__line--second">Electrical</span>
      <span class="brand__line brand__line--third">Solutions</span>
    </h1>

    <div class="person">
      <p class="person__name">OWEN PLATT</p>
      <p class="person__role">Licensed Electricans</p>
    </div>

    <p class="region">Servicing CQ Region</p>

    <p class="contact__phone">0438 516 274</p>
    <p class="contact__email">Email: admin@dorvelelectrical.example</p>
    <p class="licence">Lic No. 58342</p>
  </div>
</body>
</html>
```